Design a double sided business card

We are looking for a clean, eye-catching, and contemporary design that enhances the brand and presents a premium, professional image. Our preference is for a brown card with black gloss detailing and embossed elements; however, we are open to creative input and design suggestions that best achieve a strong visual impact.

Please see the attached existing business card for reference. We use both black and brown colours consistently across our branding.

On sample provided

```html
<!DOCTYPE html>
<html lang="en">
<head>
<meta charset="utf-8">
<title>Steinwerk – Business Card</title>
<link href="https://fonts.googleapis.com/css2?family=Montserrat:wght@400;500;700;800&display=swap" rel="stylesheet">
<style>
  :root {
    --backdrop: #a4a4a4;
    --card-tan: #c8b59b;
    --ink: #0c0c0c;
  }
  * { box-sizing: border-box; margin: 0; padding: 0; }
  html, body { width: 1200px; height: 1200px; overflow: hidden; }
  body {
    background: var(--backdrop);
    font-family: "Montserrat", Arial, sans-serif;
    color: var(--ink);
    position: relative;
  }
  .card {
    position: absolute;
    left: 145px;
    width: 909px;
    background: var(--card-tan);
    overflow: hidden;
  }
  .card--front { top: 60px; height: 520px; }
  .card--back { top: 622px; height: 518px; display: flex; align-items: center; justify-content: center; }

  .accent-band {
    position: absolute;
    right: 0;
    width: 420px;
    height: 90px;
    background: var(--ink);
  }
  .accent-band--top { top: 0; }
  .accent-band--bottom { bottom: 0; }

  .identity { position: absolute; left: 74px; top: 96px; display: flex; align-items: center; }
  .identity__name { font-weight: 700; font-size: 32px; letter-spacing: 0.01em; }
  .identity__rule { width: 2px; height: 40px; background: var(--ink); margin: 0 12px 0 16px; }
  .identity__role { font-size: 24px; font-weight: 400; }

  .contact-list { position: absolute; left: 74px; list-style: none; }
  .contact-list--direct { top: 176px; }
  .contact-list--place { top: 331px; }
  .contact-item { display: flex; align-items: flex-start; font-size: 24px; line-height: 37px; }
  .contact-item__icon { width: 18px; height: 18px; margin: 9px 14px 0 0; flex: none; fill: var(--ink); }
  .contact-item__text { display: block; }

  .brand { position: absolute; left: 552px; top: 200px; width: 300px; display: flex; flex-direction: column; align-items: center; }
  .brand__square { width: 78px; height: 72px; border: 6px solid var(--ink); }
  .brand__name { margin-top: 16px; font-weight: 800; font-size: 33px; letter-spacing: 0.16em; }

  .brand-lockup { display: flex; align-items: center; }
  .brand-lockup__square { width: 102px; height: 94px; border: 8px solid var(--ink); }
  .brand-lockup__rule { width: 3px; height: 94px; background: var(--ink); margin: 0 22px; }
  .brand-lockup__name { font-weight: 800; font-size: 50px; letter-spacing: 0.13em; }
</style>
</head>
<body>
  <section class="card card--front">
    <div class="accent-band accent-band--top" role="img" aria-label="Black decorative accent band"></div>
    <div class="accent-band accent-band--bottom" role="img" aria-label="Black decorative accent band"></div>

    <div class="identity">
      <span class="identity__name">RAVI DHILLON</span>
      <span class="identity__rule"></span>
      <span class="identity__role">Director</span>
    </div>

    <ul class="contact-list contact-list--direct">
      <li class="contact-item">
        <svg class="contact-item__icon" viewBox="0 0 24 24"><path d="M6.6 10.8a15.1 15.1 0 0 0 6.6 6.6l2.2-2.2c.3-.3.7-.4 1-.2 1.1.4 2.3.6 3.6.6.6 0 1 .4 1 1V20c0 .6-.4 1-1 1A17 17 0 0 1 3 4c0-.6.4-1 1-1h3.5c.6 0 1 .4 1 1 0 1.3.2 2.5.6 3.6.1.3 0 .7-.2 1z"/></svg>
        <span class="contact-item__text">0800 246 7710</span>
      </li>
      <li class="contact-item">
        <svg class="contact-item__icon" viewBox="0 0 24 24"><path d="M6 2h12v5H6zM3 8h18a1 1 0 0 1 1 1v8h-4v5H6v-5H2V9a1 1 0 0 1 1-1zm5 8v4h8v-4z"/></svg>
        <span class="contact-item__text">07700900415</span>
      </li>
      <li class="contact-item">
        <svg class="contact-item__icon" viewBox="0 0 24 24"><path d="M2 5h20v14H2zm2 2v.5l8 5 8-5V7l-8 5z"/></svg>
        <span class="contact-item__text">ravi@steinwerk.co.uk</span>
      </li>
    </ul>

    <ul class="contact-list contact-list--place">
      <li class="contact-item">
        <svg class="contact-item__icon" viewBox="0 0 24 24"><path d="M12 2a10 10 0 1 0 0 20 10 10 0 0 0 0-20zm0 2c.9 1.2 1.6 2.8 2 4.5h-4c.4-1.7 1.1-3.3 2-4.5zM4.3 14a8 8 0 0 1 0-4h3.5a17 17 0 0 0 0 4zm.8 2h3a14 14 0 0 0 1.5 3.6A8 8 0 0 1 5.1 16zm3-8h-3a8 8 0 0 1 4.5-3.6A14 14 0 0 0 8.1 8zM12 20c-.9-1.2-1.6-2.8-2-4.5h4c-.4 1.7-1.1 3.3-2 4.5zm2.3-6H9.7a15 15 0 0 1 0-4h4.6a15 15 0 0 1 0 4zm.1 5.6A14 14 0 0 0 15.9 16h3a8 8 0 0 1-4.5 3.6zM16.2 14a17 17 0 0 0 0-4h3.5a8 8 0 0 1 0 4z"/></svg>
        <span class="contact-item__text">www.steinwerk.co.uk</span>
      </li>
      <li class="contact-item">
        <svg class="contact-item__icon" viewBox="0 0 24 24"><path d="M12 2a7 7 0 0 0-7 7c0 5.2 7 13 7 13s7-7.8 7-13a7 7 0 0 0-7-7zm0 9.5a2.5 2.5 0 1 1 0-5 2.5 2.5 0 0 1 0 5z"/></svg>
        <span class="contact-item__text">The Green Orchard Lane<br>Eastbridge UB4 2ZX</span>
      </li>
    </ul>

    <div class="brand">
      <span class="brand__square"></span>
      <span class="brand__name">STEINWERK</span>
    </div>
  </section>

  <section class="card card--back">
    <div class="brand-lockup">
      <span class="brand-lockup__square"></span>
      <span class="brand-lockup__rule"></span>
      <span class="brand-lockup__name">STEINWERK</span>
    </div>
  </section>
</body>
</html>
```